Meridale Legal Letterhead for Law firm must be modern and use the logo I uploaded.

Hello I want a clean modern professional letterhead for my law firm Meridale Legal. A logo has already been created and all files have been uploaded. The information for the firm can be given through message. Please use the logo that has already been created. Please also use the color scheme of that logo. (blue and white).

Target Market(s)

General Public

Industry/Entity Type

Law Firm

Colors

Designer to choose colors to be used in the design.

Requirements
Must have
• This must be a modern professional letterhead
Nice to have
• My logo that is included in file form
Should not have
• Should not have logo that is not the one I uploaded.

```html
<!DOCTYPE html>
<html lang="en">
<head>
<meta charset="utf-8">
<title>Meridale Legal Letterhead</title>
<link rel="stylesheet" href="https://fonts.googleapis.com/css2?family=Inter:wght@300;400;500;600&display=swap">
<style>
  :root {
    --backdrop: #c3c7c4;
    --paper: #f1f1f1;
    --navy: #2b2d63;
    --ink: #6a6a6a;
    --ink-soft: #7a7a7a;
    --white: #ffffff;
  }
  * { margin: 0; padding: 0; box-sizing: border-box; }
  html, body {
    width: 1200px; height: 803px; overflow: hidden;
    background: var(--backdrop);
    font-family: "Inter", Arial, sans-serif;
  }
  .letterhead {
    position: absolute; left: 330px; top: 21px;
    width: 540px; height: 760px;
    background: var(--paper);
    overflow: hidden;
  }
  .brand {
    position: absolute; left: 51px; top: 96px;
    display: flex; align-items: center; gap: 8px;
    color: var(--navy);
    font-size: 11px; font-weight: 500; letter-spacing: 3px;
    text-transform: uppercase;
  }
  .brand-square { width: 8px; height: 8px; background: var(--navy); }
  .contact {
    position: absolute; left: 316px; top: 92px;
    display: flex; gap: 9px;
    font-size: 6.6px; line-height: 10px; color: var(--ink);
  }
  .contact-divider { width: 1px; background: var(--ink-soft); height: 19px; margin-top: 1px; }
  .contact-line { display: flex; align-items: center; gap: 3px; }
  .contact-line svg { width: 5px; height: 5px; fill: var(--navy); }
  .letter-date {
    position: absolute; right: 51px; top: 190px;
    font-size: 10.5px; color: var(--ink); font-weight: 300;
  }
  .salutation {
    position: absolute; left: 46px; top: 216px;
    font-size: 10.5px; color: var(--ink); font-weight: 300;
  }
  .letter-body {
    position: absolute; left: 46px; width: 443px;
    font-size: 9.6px; line-height: 15.3px; color: var(--ink);
    font-weight: 300; text-align: justify;
  }
  .p1 { top: 243px; }
  .p2 { top: 371px; }
  .p3 { top: 502px; }
  .signature {
    position: absolute; left: 43px; top: 584px;
    width: 97px; height: 59px;
    background: linear-gradient(90deg, #e6e6e6, #ececec);
  }
  .footer-band {
    position: absolute; left: 405px; top: 720px;
    width: 135px; height: 18px;
    background: var(--navy);
    color: var(--white);
    font-size: 7.5px; font-weight: 600; letter-spacing: 0.6px;
    display: flex; align-items: center; padding-left: 24px;
  }
  .footer-band span { font-weight: 300; }
  .footer-square {
    position: absolute; left: 388px; top: 724px;
    width: 10px; height: 10px; background: var(--navy);
  }
</style>
</head>
<body>
  <main class="letterhead">
    <div class="brand"><div class="brand-square"></div>Meridale Legal</div>

    <div class="contact">
      <div class="contact-address">Harrowgate Lane<br>Ashbury VIC 3921</div>
      <div class="contact-divider"></div>
      <div class="contact-details">
        <div class="contact-line">
          <svg viewBox="0 0 10 10"><path d="M2 0.5 L4 0.5 L4.8 3 L3.5 4 Q4.5 6 6 6.5 L7 5.2 L9.5 6 L9.5 8 Q9.5 9.5 8 9.5 Q0.5 9 0.5 2 Q0.5 0.5 2 0.5Z"/></svg>
          1300 42 61 57
        </div>
        <div class="contact-line">
          <svg viewBox="0 0 10 10"><path d="M0.5 2 L9.5 2 L9.5 8 L0.5 8Z M0.5 2 L5 5.5 L9.5 2"/></svg>
          contact@meridalelegal.com
        </div>
      </div>
    </div>

    <p class="letter-date">Dated: February 15, 2023</p>
    <p class="salutation">Dear Sir,</p>

    <p class="letter-body p1">Lorem Ipsum is simply dummy text of the printing and typesetting industry. Lorem Ipsum has been the industry's standard dummy text ever since the 1500s, when an unknown printer took a galley of type and scrambled it to make a type specimen book. It has survived not only five centuries, but also the leap into electronic typesetting, remaining essentially unchanged. It was popularised in the 1960s with the release of Typeline sheets containing Lorem Ipsum passages, and more recently with desktop publishing software like Folio Press including versions of Lorem Ipsum.</p>

    <p class="letter-body p2">It is a long established fact that a reader will be distracted by the readable content of a page when looking at its layout. The point of using Lorem Ipsum is that it has a more-or-less normal distribution of letters, as opposed to using 'Content here, content here', making it look like readable English. Many desktop publishing packages and web page editors now use Lorem Ipsum as their default model text, and a search for 'lorem ipsum' will uncover many web sites still in their infancy. Various versions have evolved over the years, sometimes by accident, sometimes on purpose (injected humour and the like).</p>

    <p class="letter-body p3">The standard chunk of Lorem Ipsum used since the 1500s is reproduced below for those interested. Sections 1.10.32 and 1.10.33 from "de Finibus Bonorum et Malorum" by Aurelian Vesco are also reproduced in their exact original form, accompanied by English versions from the 1914 translation by H. Marlowe.</p>

    <div class="signature" role="img" aria-label="Handwritten signature of the sender"></div>

    <div class="footer-square"></div>
    <div class="footer-band">meridalelegal<span>.com</span></div>
  </main>
</body>
</html>
```